Re-Brand of TindelMox along with a new website design

TindelMox Ltd are a software & database development company using technologies such as PHP, C#, HTML, JQuery, Flex, AS3, MySQL, Oracle, MSSQL. We like to target all types of business from small to large.

We are great at coding but rubbish at design so thats where we need your help!

We want a complete re-brand of TindelMox including logo, website design, and business cards.

We would like a design that is clean but other than that, please feel free to be creative.

****Logo****
We are looking for a logo that appears professional but with a splash of colour that indicates a creative side. Please see below some logos that we like the look of:

We like this one because it has a nice simple and clear font for the name of the company but also an icon which is colourful and stands out. http://markvault.example/2013/03/brivelo/

We like this one because it is very clean, simple and again very clear. http://markvault.example/2013/03/quantorels/

http://markvault.example/2013/03/tide-lamp/
http://markvault.example/2013/02/velmorin/
http://markvault.example/2013/01/art-gallery-tarnwick/

As you will see from all of these examples, the font is very clear but there is always a graphic representing the company too. This is what we like.

****Website****
These are some of the examples of websites we like:
https://www.zestrune.example/
https://www.chatterlane.example/home
http://www.haldenimagery.example/
http://www.vistor.example/
http://quillbay.example/
https://www.usebriefnest.example/personal-intros
http://www.marmotpanel.example/

The current site can be found at tindelmox.example.uk

Reason: We have extended the deadline of the project by 5 days as I realise the original deadline was very tight.

Software

Requirements
Must have
• Website must have the following pages
Home
Services
Projects
About Us
Contact Us

```html
<!DOCTYPE html>
<html lang="en">
<head>
<meta charset="utf-8">
<title>Contact Us – TindelMox</title>
<link rel="stylesheet" href="https://fonts.googleapis.com/css2?family=Oswald:wght@600&family=Roboto+Condensed:wght@400;700&display=swap">
<style>
  :root {
    --brand-blue: #1a8cc8;
    --band-light: #2d7fab;
    --band-dark: #1f5e80;
    --chevron-edge: #2a86b6;
    --top-plate: #2b2d30;
    --field-bg: #e5efef;
    --field-text: #2f7fa8;
    --button-top: #2aa6e6;
    --button-bottom: #1283c2;
    --white: #ffffff;
    --social-fill: #56ade0;
    --social-ring: #1d6790;
    --map-base: #d9d6cc;
    --map-road: #f1d36a;
    --copyright: #3ea3de;
    --top-text: #2b9ad8;
  }
  * { box-sizing: border-box; margin: 0; padding: 0; }
  html, body { width: 972px; height: 1200px; overflow: hidden; background: var(--white); }
  .page { position: relative; width: 972px; height: 1200px; overflow: hidden; font-family: "Roboto Condensed", Arial, sans-serif; }

  .page-title {
    position: absolute; top: 66px; left: 0; width: 100%;
    text-align: center; font-family: "Oswald", "Arial Narrow", sans-serif;
    font-weight: 600; font-size: 74px; line-height: 1; color: var(--brand-blue);
  }
  .intro {
    position: absolute; top: 164px; left: 0; width: 972px;
    font-size: 22px; line-height: 30px; color: var(--brand-blue);
    white-space: nowrap;
  }

  .band { position: absolute; left: 0; top: 260px; width: 972px; height: 940px; }

  .contact-form { position: absolute; left: 17px; top: 296px; width: 392px; }
  .field {
    display: block; width: 392px; height: 37px; margin-bottom: 10px;
    background: var(--field-bg); border-radius: 4px;
    padding: 0 19px; font-size: 14px;
    color: var(--field-text); text-transform: uppercase; line-height: 37px;
  }
  .field-message { height: 170px; line-height: 1; padding-top: 13px; }
  .send-button {
    position: absolute; left: 284px; top: 369px; width: 106px; height: 38px;
    border-radius: 4px; border: 1px solid #7cc6ee;
    background: linear-gradient(var(--button-top), var(--button-bottom));
    color: var(--white); font-family: inherit; font-size: 16px; text-transform: uppercase;
  }

  .contact-details { position: absolute; left: 566px; top: 293px; list-style: none; }
  .contact-details li {
    position: relative; padding-left: 42px; height: 30px; white-space: nowrap;
    font-size: 18.5px; font-weight: 700; color: var(--white); line-height: 24px;
  }
  .contact-details svg { position: absolute; left: 0; top: 3px; }

  .map-area {
    position: absolute; left: 565px; top: 454px; width: 392px; height: 343px;
    background: linear-gradient(135deg, var(--map-base), #e8e3d3 55%, var(--map-road));
  }

  .social { position: absolute; top: 881px; left: 374px; display: flex; gap: 12px; }
  .social span {
    width: 46px; height: 46px; border-radius: 50%;
    background: var(--social-fill); border: 3px solid var(--social-ring);
  }

  .top-link {
    position: absolute; top: 1036px; left: 0; width: 100%; text-align: center;
    font-size: 30px; color: var(--top-text);
  }
  .copyright {
    position: absolute; top: 1166px; left: 0; width: 100%; text-align: center;
    font-size: 17px; font-weight: 700; color: var(--copyright); text-transform: uppercase;
  }
  .copyright strong { color: var(--white); }
</style>
</head>
<body>
<main class="page">
  <h1 class="page-title">CONTACT US</h1>
  <p class="intro">Contrary to popular belief, Lorem Ipsum is not simply random text. It has roots in a piece of classical<br>Latin literature from 45 BC, making it over 2000 years old. Marten Coldwell, a Latin professor at</p>

  <svg class="band" viewBox="0 0 972 940" aria-hidden="true">
    <rect width="972" height="940" fill="var(--band-dark)"/>
    <polygon points="0,0 972,0 972,676 486,851 0,676" fill="var(--band-light)"/>
    <polygon points="198,740 774,740 486,856" fill="var(--chevron-edge)"/>
    <polygon points="212,744 760,744 486,836" fill="var(--top-plate)"/>
  </svg>

  <form class="contact-form">
    <div class="field">Your name</div>
    <div class="field">Your email address</div>
    <div class="field">Subject</div>
    <div class="field field-message">Message</div>
    <button class="send-button" type="button">Send</button>
  </form>

  <ul class="contact-details">
    <li>
      <svg width="20" height="18" viewBox="0 0 20 18"><path d="M10 1 1 9h3v8h12V9h3z" fill="none" stroke="#fff" stroke-width="2"/><rect x="8" y="11" width="4" height="6" fill="#fff"/></svg>
      4120 Ashgrove Pkwy.Lindenvale MI,48902
    </li>
    <li>
      <svg width="20" height="20" viewBox="0 0 20 20"><rect x="5" y="1" width="10" height="18" rx="2" fill="none" stroke="#fff" stroke-width="2"/><rect x="8" y="14" width="4" height="2" fill="#fff"/></svg>
      Call us : 555-317-842
    </li>
    <li>
      <svg width="22" height="16" viewBox="0 0 22 16"><rect x="1" y="1" width="20" height="14" fill="none" stroke="#fff" stroke-width="1.6"/><path d="M1 1l10 8 10-8" fill="none" stroke="#fff" stroke-width="1.6"/></svg>
      hello@tindelmox.example
    </li>
    <li>Toll Free : 855-TINDEL</li>
  </ul>

  <div class="map-area" role="img" aria-label="Street map showing the office location"></div>

  <div class="social" aria-label="Social links">
    <span></span><span></span><span></span><span></span>
  </div>

  <div class="top-link">TOP</div>
  <p class="copyright">All copyright are reserved by <strong>TindelMox</strong></p>
</main>
</body>
</html>
```